Kelport Tailwind Shuttle Co needs a website

We need a logo and website built for our little business. We transport Stand Up Paddle Boarders and Ocean Ski Paddlers from Byron Bay along the coast to places like Ocean Shores, Lennox Head, Ballina where they get out of the bus, hit the ocean and paddle back with the wind to Byron Bay. The website would need a link to a book now button, with a page that allows for the Byron Bay weather,wind forecast on it. Also a side bar that links to our Chatterbook page. We would like a weekly schedule of bus times on the website as well,

For themes I really like a ocean based hawaii styled theme if possible. Something that portrays the lifestyle and enjoyment people can have in the ocean. Perhaps a banner image that scrolls where we could also add photos as well over time of the business
Updates

Hi Designers have made the payment non refundable so someone will definitely be getting paid

cheers

Industry/Entity Type

Business

Colors
86acd3
3377b5
35a7d7
0392ce
ffffff
faee3f

Requirements
Nice to have
• Good Imagery of Byron Bay and coastline, I will provide some
A nice logo for the site
Link to a bus timetable where the client can book now, ( i use Bookvo bookings software so can get it to link to the site

```html
<!DOCTYPE html>
<html lang="en">
<head>
<meta charset="utf-8">
<title>Kelport Tailwind Shuttle Co</title>
<link href="https://fonts.googleapis.com/css2?family=Open+Sans:wght@400;600;700&display=swap" rel="stylesheet">
<style>
:root{
  --sky-top:#1f86d6;
  --sky-mid:#4aa6e6;
  --sea:#1aa0c8;
  --sea-light:#7fd0df;
  --sand:#d9bb8f;
  --sand-dark:#cfae7f;
  --brand-blue:#0b74c4;
  --nav-text:#3b3b3b;
  --heading:#0e3c5c;
  --body-text:#777777;
  --table-bg:#ececec;
  --table-line:#d6d6d6;
  --table-text:#555555;
  --white:#ffffff;
  --social-bg:#213a8f;
  --cta-top:#ff8a1c;
  --cta-bottom:#f24d05;
  --footer-text:#4b3b2a;
}
*{margin:0;padding:0;box-sizing:border-box}
html,body{width:1183px;height:1200px;overflow:hidden}
body{font-family:"Open Sans",Arial,sans-serif;position:relative;background:var(--sand)}
.backdrop{position:absolute;inset:0;background:linear-gradient(180deg,var(--sky-top) 0%,var(--sky-mid) 22%,#86c6ee 36%,var(--sea) 42%,var(--sea-light) 55%,#bfe3e3 62%,var(--sand) 70%,var(--sand-dark) 100%)}
.social-link{position:absolute;left:876px;top:39px;width:178px;height:27px;background:var(--social-bg);border-radius:3px;color:var(--white);font-size:12px;font-weight:600;display:flex;align-items:center;text-decoration:none;border:1px solid #14286b}
.social-link .chip{width:13px;height:13px;background:var(--white);margin:0 9px 0 10px;border-radius:2px}
.site-header{position:absolute;left:129px;top:77px;width:926px;height:73px;background:linear-gradient(180deg,#ffffff,#eeeeee);border:1px solid #dcdcdc}
.brand{position:absolute;left:14px;top:12px;width:130px;font-size:15px;line-height:18px;font-weight:700;color:var(--brand-blue)}
.main-nav{position:absolute;left:322px;top:28px;display:flex;gap:28px}
.main-nav a{font-size:15px;font-weight:600;color:var(--nav-text);text-decoration:none;letter-spacing:.2px}
.main-nav a.current{color:var(--brand-blue)}
.book-now{position:absolute;left:792px;top:18px;width:114px;height:40px;border-radius:3px;background:linear-gradient(180deg,var(--cta-top),var(--cta-bottom));color:var(--white);font-size:15px;font-weight:700;display:flex;align-items:center;justify-content:center;text-decoration:none;box-shadow:0 2px 2px rgba(0,0,0,.25)}
.hero-slider{position:absolute;left:129px;top:159px;width:925px;height:417px;overflow:hidden}
.hero-photo{position:absolute;inset:0;background:radial-gradient(ellipse at 24% 12%,#fff3b0 0%,#f2b94c 10%,transparent 32%),linear-gradient(180deg,#c9a878 0%,#dcb57a 14%,#6d6046 17%,#4d4638 30%,#2d2b26 60%,#1d1c1a 100%)}
.slider-arrow{position:absolute;top:331px;width:59px;height:59px}
.slider-arrow.prev{left:150px}.slider-arrow.next{left:983px}
.section-title{position:absolute;font-size:15px;font-weight:700;color:var(--heading);letter-spacing:.1px}
.welcome-panel{position:absolute;left:128px;top:634px;width:612px;height:466px;background:var(--white)}
.welcome-photo{position:absolute;left:11px;top:10px;width:588px;height:282px;background:linear-gradient(180deg,#5d86b8 0%,#9cb6d2 38%,#3f6a55 46%,#2c6f9a 52%,#246da0 100%)}
.welcome-text{position:absolute;left:11px;top:314px;width:596px;font-size:10.4px;line-height:23.8px;color:var(--body-text)}
.schedule{position:absolute;left:757px;top:634px;width:298px;border-collapse:collapse;background:var(--table-bg);font-size:12px;color:var(--table-text)}
.schedule th{height:47px;color:var(--brand-blue);font-weight:600;font-size:12.5px;border-bottom:1px solid var(--table-line);white-space:nowrap}
.schedule th svg{vertical-align:-4px;margin-right:4px}
.schedule td{height:47px;text-align:center;border-top:1px solid var(--table-line)}
.schedule th+th,.schedule td+td{border-left:1px solid var(--table-line)}
.weather-widget{position:absolute;left:757px;top:979px;width:298px;height:120px;background:var(--white);color:#666}
.weather-place{position:absolute;left:13px;top:6px;font-size:12px;color:#666}
.weather-meta{position:absolute;left:13px;top:21px;font-size:8px;line-height:10px;color:#777}
.weather-temp{position:absolute;left:52px;top:46px;font-size:32px;color:#222;line-height:34px}
.weather-unit{position:absolute;left:90px;top:55px;font-size:7px;color:#3355bb}
.weather-stats{position:absolute;left:150px;top:53px;font-size:7.5px;line-height:11px;color:#777}
.weather-tabs{position:absolute;left:150px;top:96px;display:flex;border:1px solid #ccc;font-size:6px}
.weather-tabs span{padding:3px 6px;background:#f2f2f2;border-left:1px solid #ccc}
.weather-tabs span:first-child{border-left:0;background:#ddd;font-weight:700}
.footer-nav{position:absolute;left:129px;top:1124px;font-size:12.5px;color:var(--footer-text)}
.footer-nav a{color:var(--footer-text);text-decoration:none}
.footer-nav .sep{margin:0 13px}
.copyright{position:absolute;left:130px;top:1158px;font-size:12.5px;color:var(--footer-text)}
.partner{position:absolute;left:927px;top:1137px;display:flex;align-items:center;gap:10px;color:var(--white);font-size:26px;font-weight:700}
.partner .dot{width:30px;height:30px;border-radius:50%;background:var(--white)}
</style>
</head>
<body>
<div class="backdrop" role="img" aria-label="Tropical beach background: blue sky, turquoise ocean waves and golden sand"></div>

<a class="social-link" href="#"><span class="chip"></span>Connect with Chatterbook</a>

<header class="site-header">
  <div class="brand">Kelport Tailwind Shuttle Co</div>
  <nav class="main-nav">
    <a class="current" href="#">HOME</a>
    <a href="#">ABOUT US</a>
    <a href="#">SERVICES</a>
    <a href="#">FAQ’S</a>
    <a href="#">CONTACT US</a>
  </nav>
  <a class="book-now" href="#">BOOK NOW</a>
</header>

<section class="hero-slider">
  <div class="hero-photo" role="img" aria-label="Sunset over calm water seen from the bow of an ocean ski, hills and a yacht on the horizon"></div>
</section>
<svg class="slider-arrow prev" viewBox="0 0 60 60"><circle cx="30" cy="30" r="29" fill="#fff" fill-opacity=".85"/><path d="M34 17 L21 30 L34 43" stroke="#555" stroke-width="7" fill="none" stroke-linecap="round" stroke-linejoin="round"/></svg>
<svg class="slider-arrow next" viewBox="0 0 60 60"><circle cx="30" cy="30" r="29" fill="#fff" fill-opacity=".85"/><path d="M26 17 L39 30 L26 43" stroke="#555" stroke-width="7" fill="none" stroke-linecap="round" stroke-linejoin="round"/></svg>

<h2 class="section-title" style="left:129px;top:598px">WELCOME TO BUS BOOKING SERVICE</h2>
<article class="welcome-panel">
  <div class="welcome-photo" role="img" aria-label="Ocean ski paddler on blue water in front of a green headland with a lighthouse"></div>
  <p class="welcome-text">Lorem Ipsum is simply dummy text of the printing and typesetting industry. Lorem Ipsum has been the industry's standard dummy text ever since the 1500s, when an unknown printer took a galley of type and scrambled it to make a type specimen book. It has survived not only five centuries, but also the leap into electronic typesetting . Lorem Ipsum is simply dummy text of the printing and typesetting industry. Lorem Ipsum has been the industry's standard dummy text ever since the 1500s, when an unknown printer took a galley of type and scrambled it to make a type specimen book. It has survived not only five centuries, but also the leap into electronic typesetting .</p>
</article>

<h2 class="section-title" style="left:757px;top:598px">BUS SCHEDULES</h2>
<table class="schedule">
  <thead>
    <tr>
      <th style="width:95px"><svg width="16" height="18" viewBox="0 0 16 18"><rect x="1" y="1" width="14" height="13" rx="3" fill="#555"/><rect x="3" y="3" width="10" height="5" fill="#ececec"/><circle cx="4.5" cy="11" r="1.3" fill="#ececec"/><circle cx="11.5" cy="11" r="1.3" fill="#ececec"/><rect x="2" y="14" width="3" height="3" fill="#555"/><rect x="11" y="14" width="3" height="3" fill="#555"/></svg>DEPART</th>
      <th style="width:94px"><svg width="16" height="18" viewBox="0 0 16 18"><rect x="1" y="1" width="14" height="13" rx="3" fill="#555"/><rect x="3" y="3" width="10" height="5" fill="#ececec"/><circle cx="4.5" cy="11" r="1.3" fill="#ececec"/><circle cx="11.5" cy="11" r="1.3" fill="#ececec"/><rect x="2" y="14" width="3" height="3" fill="#555"/><rect x="11" y="14" width="3" height="3" fill="#555"/></svg>ARRIVE</th>
      <th><svg width="18" height="18" viewBox="0 0 18 18"><circle cx="9" cy="9" r="7.5" fill="none" stroke="#555" stroke-width="1.6"/><path d="M9 4.5 V9 H12.5" stroke="#555" stroke-width="1.6" fill="none"/></svg>TRAVEL TIME</th>
    </tr>
  </thead>
  <tbody>
    <tr><td>13:52</td><td>15:29</td><td>1 h 37 mins</td></tr>
    <tr><td>13:52</td><td>15:29</td><td>1 h 37 mins</td></tr>
    <tr><td>13:52</td><td>15:29</td><td>1 h 37 mins</td></tr>
    <tr><td>13:52</td><td>15:29</td><td>1 h 37 mins</td></tr>
    <tr><td>13:52</td><td>15:29</td><td>1 h 37 mins</td></tr>
  </tbody>
</table>

<h2 class="section-title" style="left:757px;top:943px">BAYRON BAY WEATHER</h2>
<div class="weather-widget">
  <div class="weather-place">Byron Bay NSW, Australia</div>
  <div class="weather-meta">Tuesday 6:00 pm<br>Overcast</div>
  <svg style="position:absolute;left:14px;top:56px" width="32" height="20" viewBox="0 0 32 20"><path d="M7 18 a6 6 0 0 1 1-11 a8 8 0 0 1 15 1 a5 5 0 0 1 2 10 z" fill="#cfcfcf"/></svg>
  <div class="weather-temp">23</div>
  <div class="weather-unit">°C | °F</div>
  <div class="weather-stats">Precipitation: 10%<br>Humidity: 84%<br>Wind: 10 km/h</div>
  <div class="weather-tabs"><span>Temperature</span><span>Precipitation</span><span>Wind</span></div>
</div>

<nav class="footer-nav">
  <a href="#">Home</a><span class="sep">|</span><a href="#">About Us</a><span class="sep">|</span><a href="#">Services</a><span class="sep">|</span><a href="#">FAQ’s</a><span class="sep">|</span><a href="#">Contact Us</a>
</nav>
<p class="copyright">Copyright ©2013 Company Name &nbsp; - All rights reserved</p>

<div class="partner"><span class="dot"></span>Bookvo</div>
</body>
</html>
```